Business card and stationary for tattoo photography company
Velvet Harbor Photography
Business card and stationary for tattoo photography company - Photography
Creative Brief
Modern
Rolf Lindqvist
Photographer / Owner
4630 Marlow Ave W Brindlecove, OR 97487
rolf@velvetharborphotoworks.com
www.velvetharborphotoworks.com
Strength, Elegance, and Beauty

```html
<!DOCTYPE html>
<html lang="en">
<head>
<meta charset="utf-8">
<title>Velvet Harbor Photography – Business Card</title>
<link rel="stylesheet" href="https://fonts.googleapis.com/css2?family=Lato:wght@300;400;700&display=swap">
<style>
  :root {
    --backdrop: #2b2b2d;
    --card-black: #0f0f10;
    --card-white: #f1f1f1;
    --accent-red: #c8141c;
    --text-light: #f4f4f4;
    --text-muted: #9a9a9a;
    --text-dark: #444444;
    --skin-warm: #b48a78;
    --ink-violet: #5a4a66;
  }
  * { margin: 0; padding: 0; box-sizing: border-box; }
  html, body { width: 1200px; height: 794px; overflow: hidden; }
  body {
    background: var(--backdrop);
    font-family: "Lato", sans-serif;
    position: relative;
  }
  .card {
    position: absolute;
    top: 242px;
    width: 540px;
    height: 310px;
    border-radius: 18px;
    overflow: hidden;
    box-shadow: 0 10px 30px rgba(0,0,0,.45);
  }
  /* ---------- Front ---------- */
  .card--front { left: 40px; background: var(--card-black); }
  .front-photo {
    position: absolute; left: 0; top: 0; width: 270px; height: 100%;
    background: linear-gradient(100deg, var(--ink-violet) 0%, var(--skin-warm) 40%, #6d574f 70%, var(--card-black) 100%);
  }
  .front-brand {
    position: absolute; left: 250px; right: 20px; top: 92px; text-align: center;
  }
  .brand-name {
    color: var(--text-light);
    font-weight: 300;
    font-size: 30px;
    letter-spacing: 1px;
    line-height: 1.1;
    white-space: nowrap;
  }
  .brand-sub {
    color: var(--text-light);
    font-weight: 300;
    font-size: 11px;
    letter-spacing: 5px;
    text-transform: uppercase;
    margin-top: 6px;
  }
  .tagline {
    color: var(--text-light);
    font-size: 13px;
    margin-top: 22px;
    letter-spacing: .5px;
  }
  .front-url {
    position: absolute; right: 34px; bottom: 52px;
    color: var(--text-muted); font-size: 10px; letter-spacing: .5px;
  }
  /* ---------- Back ---------- */
  .card--back { left: 620px; background: var(--card-white); }
  .back-band { position: absolute; left: 0; top: 0; width: 540px; height: 310px; }
  .back-photo {
    position: absolute; left: 32px; top: 0; width: 118px; height: 150px;
    background: linear-gradient(160deg, #3a2c28 0%, var(--skin-warm) 55%, #2a1f1c 100%);
  }
  .back-brand { position: absolute; left: 190px; top: 48px; width: 300px; text-align: center; }
  .back-brand .brand-name { font-size: 27px; }
  .person { position: absolute; left: 34px; top: 206px; }
  .person-name { color: var(--accent-red); font-size: 18px; font-weight: 400; }
  .person-role { color: var(--text-muted); font-size: 11px; margin-top: 3px; }
  .contact {
    position: absolute; right: 22px; top: 196px;
    list-style: none; text-align: right;
    color: var(--text-dark); font-size: 11px; line-height: 17px;
  }
  .contact li { display: flex; justify-content: flex-end; align-items: center; gap: 8px; white-space: nowrap; }
  .contact .icon { width: 11px; height: 11px; flex: none; }
  .contact .spacer { width: 11px; flex: none; }
</style>
</head>
<body>

<section class="card card--front" aria-label="Business card front">
  <div class="front-photo" role="img" aria-label="Photograph of a tattooed model seated in soft light"></div>
  <div class="front-brand">
    <div class="brand-name">Velvet Harbor</div>
    <div class="brand-sub">Photography</div>
    <p class="tagline">Strength, Elegance, and Beauty</p>
  </div>
  <div class="front-url">www.velvetharborphotoworks.com</div>
</section>

<section class="card card--back" aria-label="Business card back">
  <svg class="back-band" viewBox="0 0 540 310" aria-hidden="true">
    <path d="M0 0 H540 V138 C420 150 300 176 180 180 C110 182 50 178 0 174 Z" fill="var(--card-black)"/>
    <path d="M0 174 C50 178 110 182 180 180 C300 176 420 150 540 138 V148 C420 162 300 188 180 190 C110 192 50 188 0 184 Z" fill="var(--accent-red)"/>
  </svg>
  <div class="back-photo" role="img" aria-label="Photograph of a tattooed model's back"></div>
  <div class="back-brand">
    <div class="brand-name">Velvet Harbor</div>
    <div class="brand-sub">Photography</div>
  </div>
  <div class="person">
    <div class="person-name">Rolf Lindqvist</div>
    <div class="person-role">Photographer / Owner</div>
  </div>
  <ul class="contact">
    <li>4630 Marlow Ave W<span class="spacer"></span></li>
    <li>Brindlecove, OR 97487
      <svg class="icon" viewBox="0 0 12 12" aria-hidden="true"><circle cx="6" cy="6" r="6" fill="var(--accent-red)"/><path d="M6 2.5a2 2 0 0 0-2 2c0 1.6 2 4.5 2 4.5s2-2.9 2-4.5a2 2 0 0 0-2-2z" fill="#fff"/></svg></li>
    <li>(555) 014-2290
      <svg class="icon" viewBox="0 0 12 12" aria-hidden="true"><circle cx="6" cy="6" r="6" fill="var(--accent-red)"/><path d="M4 3l1.2 1.5-.6.8a4 4 0 0 0 2.1 2.1l.8-.6L9 8l-.7 1C6 9 3 6 3 3.7z" fill="#fff"/></svg></li>
    <li>rolf@velvetharborphotoworks.com
      <svg class="icon" viewBox="0 0 12 12" aria-hidden="true"><circle cx="6" cy="6" r="6" fill="var(--accent-red)"/><rect x="3" y="4" width="6" height="4" fill="#fff"/><path d="M3 4l3 2.2L9 4" stroke="var(--accent-red)" stroke-width=".7" fill="none"/></svg></li>
    <li>www.velvetharborphotoworks.com
      <svg class="icon" viewBox="0 0 12 12" aria-hidden="true"><circle cx="6" cy="6" r="6" fill="var(--accent-red)"/><circle cx="6" cy="6" r="3" fill="none" stroke="#fff" stroke-width=".8"/><path d="M3 6h6M6 3v6" stroke="#fff" stroke-width=".7"/></svg></li>
  </ul>
</section>

</body>
</html>
```